Law Firm Website

I currently have a temporary site that I created myself at www.kbrandellegal.net (hosted by hostpivot). I am generally happy with the content.

My permanent website just has basic information right now: www.kbrandellegal.com (hosted by cloudperch). I want to take the general content from the temporary website and have a more professional looking website on the permanent website. I want it in Wordpress format. I want a link to my blog: www.rivetsand.com. I want it to work on pads and smart phones. My number and e-mail address should be available on every page. The idea is to feature the potential client more than the lawyer.
Updates

Several of the designs are good. I would like the front page to have my number and address at the top (and at the top of every page) and to identify my law firm as "Law Office of Karen J. Brandell". No need to include "kbrandellegal" as that is just the web address. I like showing the most recent blog posts on the front page. I don't need video. No need to emphasize office hours or map location on the front page (that could be under a contact button). My picture should be somewhere. I would like an image from Boston on the front page if we can find one that is not copyright protected. No images of gavels or scales of justice. See some of the sample websites I listed in previous messages. Thanks!

Reason: I need more time to evaluate designs.

Reason: Designers apparently misunderstood and provided design that was not wordpress.

Industry/Entity Type

Law Firm

```html
<!DOCTYPE html>
<html lang="en">
<head>
<meta charset="utf-8">
<title>Law Office of Karen J. Brandell</title>
<link rel="stylesheet" href="https://fonts.googleapis.com/css2?family=Arimo:wght@400;700&family=Cinzel:wght@700&family=PT+Sans&family=Archivo+Narrow&display=swap">
<style>
  :root {
    --page: #ffffff;
    --ink: #222222;
    --ink-soft: #333333;
    --muted: #666666;
    --brand-blue: #0d56a6;
    --nav-top: #f2f2f2;
    --nav-bottom: #b9b9b9;
    --pill: #e6e6e6;
    --footer: #000000;
    --footer-text: #cfcfcf;
    --bg-edge: #4a4a4a;
    --bg-mid: #c4c4c4;
  }
  * { margin: 0; padding: 0; box-sizing: border-box; }
  html, body { width: 1198px; height: 1200px; overflow: hidden; }
  body {
    position: relative;
    font-family: "Arimo", Arial, sans-serif;
    color: var(--ink);
    background: linear-gradient(90deg, var(--bg-edge) 0%, var(--bg-mid) 30%, var(--bg-mid) 70%, var(--bg-edge) 100%);
  }
  h1, h2, h3 { font-weight: 400; }
  .page { position: absolute; left: 138px; top: 0; width: 922px; height: 1090px; background: var(--page); }
  .abs { position: absolute; white-space: nowrap; }

  /* header */
  .firm-name { left: 152px; top: 30px; font-family: "Cinzel", Georgia, serif; font-weight: 700; font-size: 24px; letter-spacing: .5px; color: #111; }
  .firm-rule { left: 152px; top: 66px; width: 290px; height: 1px; background: #555; }
  .firm-sub { left: 152px; top: 76px; width: 290px; text-align: center; font-size: 13px; color: #222; letter-spacing: .3px; }
  .call { right: 160px; top: 42px; font-family: "PT Sans", sans-serif; }
  .call .label { font-size: 19px; color: var(--brand-blue); margin-right: 6px; }
  .call .number { font-size: 31px; color: #111; letter-spacing: .5px; }
  .contact-line { right: 160px; top: 84px; font-size: 12px; color: var(--muted); }

  /* navigation */
  .nav { left: 129px; top: 109px; width: 940px; height: 44px; background: linear-gradient(var(--nav-top), var(--nav-bottom)); }
  .nav-fold { top: 98px; width: 0; height: 0; border-bottom: 11px solid #111; }
  .nav-fold.left { left: 129px; border-left: 9px solid transparent; }
  .nav-fold.right { left: 1060px; border-right: 9px solid transparent; }
  .nav ul { list-style: none; }
  .nav li { position: absolute; top: 9px; font-size: 13.5px; color: #111; height: 26px; line-height: 26px; white-space: nowrap; }
  .nav li.home { background: var(--brand-blue); color: #fff; border-radius: 2px; width: 63px; text-align: center; }

  .hero { left: 138px; top: 153px; width: 922px; height: 386px; background: linear-gradient(180deg, #0a3b8a 0%, #1e67d6 35%, #123b78 62%, #05080e 85%, #000 100%); }

  /* welcome */
  .welcome-title { left: 155px; top: 564px; font-family: "Cinzel", Georgia, serif; font-weight: 700; font-size: 22px; letter-spacing: 1.5px; color: #111; }
  .intro { left: 158px; top: 611px; width: 540px; white-space: normal; font-size: 12.5px; line-height: 20.3px; color: var(--ink-soft); }
  .intro p + p { margin-top: 20px; }
  .tower { left: 158px; top: 818px; width: 187px; height: 193px; background: linear-gradient(135deg, #1f3f86 0%, #5e7fb6 45%, #d9e3ee 60%, #6b6e74 100%); }
  .attack-title { left: 359px; top: 816px; font-family: "Archivo Narrow", sans-serif; font-size: 23px; color: var(--brand-blue); }
  .attack-list { left: 362px; top: 853px; list-style: none; font-size: 12.5px; font-weight: 700; letter-spacing: .6px; color: #222; }
  .attack-list li { height: 24px; }

  /* focus areas */
  .focus-title { left: 743px; top: 563px; font-size: 25px; color: var(--brand-blue); }
  .focus-list { left: 741px; top: 610px; list-style: none; width: 285px; }
  .focus-list li { height: 25px; line-height: 25px; padding-left: 8px; background: var(--pill); border-radius: 3px; font-size: 12.5px; color: #222; margin-bottom: 11.9px; }

  /* blog posts */
  .blog { left: 746px; top: 852px; width: 280px; white-space: normal; }
  .blog-title { font-size: 17px; color: var(--brand-blue); margin-bottom: 8px; }
  .blog-list { list-style: none; }
  .blog-list li { border-top: 1px solid #dddddd; padding: 7px 0; }
  .blog-list .post { font-size: 12.5px; color: #222; }
  .blog-list .date { font-size: 11px; color: var(--muted); margin-top: 2px; }
  .blog-more { font-size: 11.5px; color: var(--brand-blue); border-top: 1px solid #dddddd; padding-top: 7px; }

  /* footer */
  .skyline { left: 405px; top: 1068px; width: 374px; height: 22px; background: #000; }
  .footer { left: 0; top: 1090px; width: 1198px; height: 110px; background: var(--footer); }
  .copyright { left: 158px; top: 1142px; font-size: 13px; color: var(--footer-text); }
  .social { left: 493px; top: 1138px; }
  .newsletter { left: 779px; top: 1140px; width: 254px; height: 29px; display: flex; }
  .newsletter .field { flex: 1; background: #fff; border: 1px solid #bbb; font-size: 11px; color: #777; padding-left: 8px; line-height: 27px; }
  .newsletter .go { width: 30px; background: var(--brand-blue); color: #fff; font-size: 12px; font-weight: 700; text-align: center; line-height: 29px; }
</style>
</head>
<body>
  <div class="page"></div>

  <header>
    <div class="abs firm-name">KAREN J. BRANDELL</div>
    <div class="abs firm-rule"></div>
    <div class="abs firm-sub">LAW OFFICE OF KAREN J. BRANDELL</div>
    <div class="abs call"><span class="label">Call Us Today:</span><span class="number">617 555-0142</span></div>
    <div class="abs contact-line">120 Tremont Street, Suite 400, Boston, MA 02108 · kjb@kbrandellegal.com</div>
  </header>

  <div class="abs nav-fold left"></div>
  <div class="abs nav-fold right"></div>
  <nav class="abs nav">
    <ul>
      <li class="home" style="left:24px">Home</li>
      <li style="left:116px">Why Hire Me?</li>
      <li style="left:244px">Success Stories</li>
      <li style="left:384px">Practice Areas</li>
      <li style="left:516px">Representative Clients</li>
      <li style="left:692px">Services Provided</li>
      <li style="left:840px">Contact Us</li>
    </ul>
  </nav>

  <div class="abs hero" role="img" aria-label="Night photograph of a domed capitol building lit against a deep blue sky"></div>

  <main>
    <h1 class="abs welcome-title">Welcome to Our Law Office</h1>
    <div class="abs intro">
      <p>Lorem Ipsum is simply dummy text of the printing and typesetting industry. Lorem Ipsum has been the industry's standard dummy text ever since the 1500s, when an unknown printer took a galley of type and scrambled it to make a type specimen book.</p>
      <p>It has survived not only five centuries, but also the leap into electronic typesetting, remaining essentially unchanged. It was popularised in the 1960s with the release of Transfix sheets containing Lorem Ipsum passages, and more recently with desktop publishing software like Folio PageSetter with the release of Transfix sheets containing Lorem Ipsum passages, and more recently with desktop publishing software like including versions of Lorem Ipsum.</p>
    </div>

    <div class="abs tower" role="img" aria-label="Photograph of a glass office tower seen from below"></div>
    <h2 class="abs attack-title">Your business is under constant attack.</h2>
    <ul class="abs attack-list">
      <li>Contract review and drafting.</li>
      <li>Employee handbooks.</li>
      <li>Non-Compete Agreements.</li>
      <li>Employee Hiring and Firing.</li>
      <li>Dealing with Rogue Employees.</li>
      <li>Interference with Contractual Relations.</li>
      <li>Breach of Contract.</li>
    </ul>

    <h2 class="abs focus-title">Focus Practice Areas</h2>
    <ul class="abs focus-list">
      <li>Employment Counseling and Litigation</li>
      <li>Hiring and Firing.</li>
      <li>Wage and Hour Issues.</li>
      <li>Noncompetes.</li>
      <li>Sexual Harassment.</li>
      <li>Leave Issues under the ADA, FMLA &amp; State Law.</li>
    </ul>

    <section class="abs blog">
      <h2 class="blog-title">Recent Blog Posts</h2>
      <ul class="blog-list">
        <li><div class="post">Updating Your Employee Handbook</div><div class="date">March 12</div></li>
        <li><div class="post">When Is a Noncompete Enforceable?</div><div class="date">February 27</div></li>
        <li><div class="post">Paying Overtime the Right Way</div><div class="date">February 9</div></li>
      </ul>
      <div class="blog-more">Read more at www.rivetsand.com</div>
    </section>
  </main>

  <div class="abs skyline" role="img" aria-label="City skyline silhouette"></div>

  <footer class="abs footer"></footer>
  <div class="abs copyright">© Law Office of Karen J. Brandell</div>
  <svg class="abs social" width="210" height="38" viewBox="0 0 210 38" role="img" aria-label="Social media links">
    <defs>
      <radialGradient id="socialFill" cx="50%" cy="35%" r="60%">
        <stop offset="0%" stop-color="#f4f4f4"/>
        <stop offset="100%" stop-color="#a9a9a9"/>
      </radialGradient>
    </defs>
    <g stroke="#2a2a2a" stroke-width="3" fill="url(#socialFill)">
      <circle cx="18" cy="18" r="16"/>
      <circle cx="61" cy="18" r="16"/>
      <circle cx="103" cy="18" r="16"/>
      <circle cx="146" cy="18" r="16"/>
      <circle cx="188" cy="18" r="16"/>
    </g>
  </svg>
  <div class="abs newsletter">
    <div class="field">Sign up to our newsletter</div>
    <div class="go">GO</div>
  </div>
</body>
</html>
```